New Advertising Company Business Card

A two sided business card. One side with logo only and the other side with my information and maybe my logo again. Looking for something unique and creative, but not too busy. Info would include my name(Marcus Fenley), President, phone number, address, email address, and website. LOGO IS THE BLUE AND WHITE ONE.

Target Market(s)

CEO/VP Level Audience

Industry/Entity Type

Business

Contact Information for Business Card

In Description.

```html
<!DOCTYPE html>
<html lang="en">
<head>
<meta charset="utf-8">
<title>Keelstone Advertising – Business Card</title>
<link href="https://fonts.googleapis.com/css2?family=Open+Sans:wght@400;600;700&display=swap" rel="stylesheet">
<style>
  :root {
    --brand-blue: #1a77c0;
    --band-blue: #1565b8;
    --ink: #2b2b2b;
    --paper: #ffffff;
    --backdrop: #ece8e2;
  }
  * { margin: 0; padding: 0; box-sizing: border-box; }
  html, body { width: 1200px; height: 1200px; overflow: hidden; }
  body {
    background: var(--backdrop);
    font-family: "Open Sans", Arial, sans-serif;
    position: relative;
  }
  .card {
    position: absolute;
    left: 250px;
    width: 700px;
    height: 400px;
    box-shadow: 0 6px 20px rgba(0,0,0,0.12);
  }
  .card--front { top: 160px; background: var(--paper); }
  .card--back { top: 640px; background: var(--brand-blue); color: var(--paper); }

  .wordmark {
    display: flex;
    align-items: center;
    justify-content: center;
    gap: 12px;
    font-weight: 600;
    letter-spacing: 0.18em;
    text-transform: uppercase;
  }
  .wordmark__dot {
    width: 16px; height: 16px; border-radius: 50%;
  }
  .card--front .wordmark {
    position: absolute; top: 62px; left: 0; right: 0;
    color: var(--brand-blue); font-size: 22px;
  }
  .card--front .wordmark__dot { background: var(--brand-blue); }

  .identity {
    position: absolute; top: 118px; left: 0; right: 0;
    text-align: center;
  }
  .identity__name {
    color: var(--brand-blue); font-weight: 700; font-size: 34px;
    text-transform: uppercase; letter-spacing: -0.01em; line-height: 1.1;
  }
  .identity__title {
    color: var(--ink); font-size: 22px; line-height: 1.3;
  }

  .band {
    position: absolute; left: 0; right: 0; top: 252px; height: 18px;
    background: var(--band-blue);
  }
  .band__icon {
    position: absolute; top: 3px; width: 12px; height: 12px;
  }
  .contacts {
    position: absolute; left: 0; right: 0; top: 270px; height: 130px;
    display: grid; grid-template-columns: repeat(3, 1fr);
  }
  .contacts__item {
    padding: 26px 20px 0;
    color: var(--band-blue);
    font-size: 15px; line-height: 1.4;
    text-align: center;
  }
  .contacts__item + .contacts__item { position: relative; }
  .contacts__item + .contacts__item::before {
    content: ""; position: absolute; left: 0; top: 0;
    width: 2px; height: 62px; background: var(--band-blue);
  }

  .card--back .wordmark {
    position: absolute; top: 160px; left: 0; right: 0;
    font-size: 26px; color: var(--paper);
  }
  .card--back .wordmark__dot { background: var(--paper); width: 18px; height: 18px; }
  .website {
    position: absolute; top: 300px; left: 0; right: 0;
    text-align: center; font-size: 16px; color: var(--paper);
  }
</style>
</head>
<body>

<section class="card card--front" aria-label="Business card front">
  <div class="wordmark"><span class="wordmark__dot"></span><span>Keelstone Advertising</span></div>
  <div class="identity">
    <div class="identity__name">Marcus Fenley</div>
    <div class="identity__title">President</div>
  </div>

  <div class="band">
    <svg class="band__icon" style="left:111px" viewBox="0 0 12 12" aria-hidden="true">
      <path d="M2.5 1 L4.5 1 L5.2 3.6 L4 4.6 Q5 7 7.4 8 L8.4 6.8 L11 7.5 L11 9.5 Q10.5 11 9 11 Q1 10 1 3 Q1 1.5 2.5 1 Z" fill="#fff"/>
    </svg>
    <svg class="band__icon" style="left:344px" viewBox="0 0 12 12" aria-hidden="true">
      <rect x="0.5" y="2" width="11" height="8" fill="#fff"/>
      <path d="M0.5 2 L6 6.5 L11.5 2" fill="none" stroke="#1565b8" stroke-width="1"/>
    </svg>
    <svg class="band__icon" style="left:577px" viewBox="0 0 12 12" aria-hidden="true">
      <path d="M6 0.5 Q10 0.5 10 4.5 Q10 7 6 11.5 Q2 7 2 4.5 Q2 0.5 6 0.5 Z" fill="#fff"/>
      <circle cx="6" cy="4.5" r="1.6" fill="#1565b8"/>
    </svg>
  </div>

  <div class="contacts">
    <div class="contacts__item">555-014-2290</div>
    <div class="contacts__item">info@keelstoneadvertising.com</div>
    <div class="contacts__item">18 Palmer Ln. Kailua,<br>HI 96734</div>
  </div>
</section>

<section class="card card--back" aria-label="Business card back">
  <div class="wordmark"><span class="wordmark__dot"></span><span>Keelstone Advertising</span></div>
  <div class="website">www.keelstoneadvertising.com</div>
</section>

</body>
</html>
```